New audiology website PSD design only - guaranteed

We need a clean and attractive website to replace an existing Audiology (hearing technology) website which will be wordpress based.
The current website is: http://pelmorahearing.com.au
They have a new logo and colors which you can find at www.quodel.net/temp/plh2018.pdf
We will no longer have a web shop in the new website
To enter the competition, we only need a sample of the home page.
The winning design will be asked to produce 2 standard page template alternatives as well (based on the winning home page design, but for a standard page layout)
The winning design must provide any photos used
We want a clean, credible site but with some warmth
Target Market(s)
All ages but needs to include the elderly
Industry/Entity Type
Medical And Science
Number of Pages Required
3 page
Look and feel
Each slider illustrates characteristics of the customer's brand and the style your logo design should communicate.

```html
<!DOCTYPE html>
<html lang="en">
<head>
<meta charset="utf-8">
<title>Pelmora Hearing – Home</title>
<link href="https://fonts.googleapis.com/css2?family=Oswald:wght@300;400;500&family=Open+Sans:wght@400;600&display=swap" rel="stylesheet">
<style>
:root{
  --orange:#e06a2b;
  --orange-dark:#c9561c;
  --ink:#3a3a3a;
  --muted:#6d6d6d;
  --line:#d9d9d9;
  --white:#ffffff;
  --charcoal:#2b2b2b;
  --nav-btn:#9a9a9a;
}
*{box-sizing:border-box;margin:0;padding:0}
html,body{width:1200px;height:2668px;overflow:hidden;background:var(--white)}
body{font-family:"Open Sans",Arial,sans-serif;color:var(--ink);position:relative}
.wrap{width:880px;margin:0 auto;position:relative}

/* header */
.topbar{height:76px;display:flex;align-items:center}
.topbar .wrap{display:flex;justify-content:space-between;align-items:center}
.brand{display:flex;align-items:center;gap:12px;font-family:"Oswald",sans-serif;font-weight:500;font-size:30px;color:var(--orange)}
.brand .dot{width:30px;height:30px;border-radius:50%;background:var(--orange)}
.contact-top{text-align:right;font-size:15px;color:var(--muted)}
.contact-top .socials{display:flex;gap:6px;justify-content:flex-end;margin-top:6px}
.contact-top .socials span{width:22px;height:22px;border-radius:50%;background:#8a8a8a}
.mainnav{height:52px;background:var(--orange)}
.mainnav ul{list-style:none;display:flex;height:52px;align-items:center;gap:30px}
.mainnav a{color:var(--white);text-decoration:none;font-size:15px}
.mainnav .account{margin-left:auto;background:var(--nav-btn);padding:9px 14px}

/* hero */
.hero{position:relative;height:640px}
.hero-photo{position:absolute;inset:0;background:linear-gradient(100deg,#1d1d1d 0%,#5c5c5c 28%,#9b9b9b 45%,#4a4a4a 70%,#262626 100%)}
.hero-title{position:absolute;left:0;right:0;top:256px;text-align:center;font-family:"Oswald",sans-serif;font-weight:300;font-size:56px;line-height:1.3;color:var(--white);letter-spacing:1px}
.hero-title em{font-style:normal;color:var(--orange)}
.hero-strip{height:16px;background:var(--orange)}

/* section headings */
.section-title{font-family:"Oswald",sans-serif;font-weight:400;font-size:34px;text-align:center;color:var(--charcoal);padding-top:24px}
.section-title::after{content:"";display:block;width:200px;height:2px;background:var(--charcoal);margin:8px auto 0}

/* services */
.services{height:440px;overflow:hidden}
.services p{font-size:13px;line-height:1.75;color:var(--muted);margin-bottom:18px}
.services .name{color:var(--orange)}
.services .p1{width:720px;margin-top:24px}
.services .p2{width:560px;margin-left:160px}
.services .p3{width:720px}
.services .icon{position:absolute}

/* newsletter */
.newsletter{position:relative;height:272px}
.newsletter-photo{position:absolute;inset:0;background:linear-gradient(90deg,#1e1e1e,#4c4c4c 45%,#6a6a6a 60%,#333 100%)}
.newsletter .wrap{display:flex;justify-content:space-between;height:272px;align-items:center}
.newsletter-copy{color:var(--white);text-align:center;width:560px}
.newsletter-copy h2{font-family:"Oswald",sans-serif;font-weight:300;font-size:36px;letter-spacing:1px;margin-bottom:18px}
.newsletter-copy p{font-size:17px;line-height:1.5;color:#e4e4e4}
.signup{width:220px;background:var(--white);padding:14px}
.signup .field{height:36px;border:1px solid var(--line);font-size:13px;color:#888;padding:9px 10px;margin-bottom:10px}
.signup .btn{height:38px;background:var(--orange);color:var(--white);font-size:13px;letter-spacing:1px;text-align:center;padding-top:10px}

/* locations */
.locations{height:760px}
.clinic{position:relative;height:300px;margin-top:48px}
.clinic + .clinic{margin-top:20px}
.clinic .row{position:absolute;left:40px;display:flex;align-items:center;gap:40px;font-size:15px;color:var(--muted);line-height:1.5}
.clinic .row svg{flex:none}
.clinic .row .txt{text-align:center;width:320px}
.clinic h3{font-family:"Open Sans",sans-serif;font-weight:600;font-size:16px;color:var(--charcoal)}
.map{position:absolute;right:20px;top:0;width:260px;height:260px;border-radius:50%;border:8px solid #eeeeee;background:radial-gradient(circle at 55% 45%,#f2e7e7,#ddd6d2 60%,#cfcac4)}

/* footer */
.footer{background:var(--orange);height:380px;color:var(--white)}
.footer .wrap{display:flex;justify-content:space-between;padding-top:22px}
.footer h4{font-family:"Oswald",sans-serif;font-weight:400;font-size:24px;text-align:center;margin-bottom:20px}
.quick{width:240px}
.quick ul{list-style:none;padding-left:40px}
.quick li{font-size:14px;line-height:2.1}
.quick li::before{content:"";display:inline-block;width:5px;height:5px;background:var(--white);border-radius:50%;margin-right:10px;vertical-align:middle}
.contact-form{width:260px}
.contact-form form{background:var(--white);padding:12px}
.contact-form .field{height:32px;border:1px solid var(--line);font-size:12px;color:#888;padding:7px 10px;margin-bottom:8px}
.contact-form .msg{height:70px}
.contact-form .btn{height:34px;background:var(--orange);color:var(--white);text-align:center;font-size:13px;padding-top:8px}
.social{width:240px}
.social .icons{display:flex;justify-content:center;gap:16px;margin-top:24px}
.social .icons span{width:52px;height:52px;border-radius:50%;border:3px solid var(--white)}
.legal{background:var(--orange-dark);height:28px;color:var(--white);font-size:11px;text-align:center;padding-top:7px}
</style>
</head>
<body>

<header class="topbar">
  <div class="wrap">
    <div class="brand"><span class="dot"></span>Pelmora Hearing</div>
    <div class="contact-top">
      Ph: (02) 5550 0148
      <div class="socials"><span></span><span></span><span></span></div>
    </div>
  </div>
</header>
<nav class="mainnav">
  <ul class="wrap">
    <li><a href="#">Our Hearing</a></li>
    <li><a href="#">Hearing Aids</a></li>
    <li><a href="#">Resources</a></li>
    <li><a href="#">Services Information</a></li>
    <li><a href="#">About Us</a></li>
    <li><a href="#">Contact Us</a></li>
    <li class="account"><a href="#">My Account</a></li>
  </ul>
</nav>

<section class="hero">
  <div class="hero-photo" role="img" aria-label="Close-up photo of an elderly man wearing a behind-the-ear hearing aid"></div>
  <h1 class="hero-title">AN INDEPENDENTLY OWNED AND MANAGED<br>PROFESSIONAL <em>AUDIOLOGY CLINIC</em></h1>
</section>
<div class="hero-strip"></div>

<section class="services">
  <div class="wrap">
    <h2 class="section-title">OUR SERVICES</h2>
    <p class="p1"><span class="name">Pelmora Hearing</span> is an independently owned and managed professional audiology clinic. Our audiologists are health care professionals specialising in diagnosing, treating and monitoring hearing disorders and balance. At Pelmora Hearing we work closely with Ear Nose and Throat specialists to ensure you receive the highest standards of medical care.</p>
    <svg class="icon" style="left:800px;top:110px" width="80" height="80" viewBox="0 0 80 80" fill="none" stroke="var(--orange)" stroke-width="6" stroke-linecap="round">
      <path d="M18 8 v22 a14 14 0 0 0 28 0 v-22"/>
      <path d="M32 44 v10 a14 14 0 0 0 28 0 v-6"/>
      <circle cx="60" cy="40" r="7"/>
    </svg>
    <p class="p2"><span class="name">Pelmora Hearing</span> use state of the art hearing and balance testing. We provide all brands of digital hearing aids, cochlear implants and assistive listening devices. We see diagnostic clients, offering hearing tests for adults and children, balance tests and auditory processing tests.</p>
    <p class="p3">At <span class="name">Pelmora Hearing</span> we are committed to excellence. We are at the forefront of providing detailed hearing and treatment options. Our team is friendly, experienced and fully accredited, and our success is measured by your satisfaction.</p>
    <svg class="icon" style="left:804px;top:296px" width="76" height="76" viewBox="0 0 76 76" fill="none" stroke="var(--orange)" stroke-width="6" stroke-linecap="round" stroke-linejoin="round">
      <circle cx="38" cy="38" r="33"/>
      <path d="M22 38 l12 12 l22 -24"/>
    </svg>
  </div>
</section>

<section class="newsletter">
  <div class="newsletter-photo" role="img" aria-label="Photo of hands typing on a laptop keyboard"></div>
  <div class="wrap">
    <div class="newsletter-copy">
      <h2>SIGN UP FOR OUR NEWSLETTER</h2>
      <p>Keep up with the latest trends and advances in hearing health.<br>Sign up for our upcoming newsletter</p>
    </div>
    <form class="signup">
      <div class="field">Email</div>
      <div class="field">First Name</div>
      <div class="field">Last Name</div>
      <div class="btn">SUBSCRIBE</div>
    </form>
  </div>
</section>

<section class="locations">
  <div class="wrap">
    <h2 class="section-title">OUR LOCATIONS</h2>

    <div class="clinic">
      <div class="row" style="top:30px">
        <svg width="48" height="56" viewBox="0 0 48 56" fill="none" stroke="var(--orange)" stroke-width="3"><path d="M24 52 C10 34 8 28 8 20 a16 16 0 0 1 32 0 c0 8 -2 14 -16 32z"/><circle cx="24" cy="20" r="6"/><path d="M6 52 h36"/></svg>
        <div class="txt"><h3>HARBOUR POINT</h3>Ground Floor, Suite 8, 14 Keel Parade<br>Harbour Point</div>
      </div>
      <div class="row" style="top:130px">
        <svg width="48" height="48" viewBox="0 0 48 48" fill="none" stroke="var(--orange)" stroke-width="3" stroke-linejoin="round"><path d="M10 6 l8 0 l4 10 l-6 4 a26 26 0 0 0 12 12 l4 -6 l10 4 v8 a4 4 0 0 1 -4 4 C20 42 6 28 6 10 a4 4 0 0 1 4 -4z"/></svg>
        <div class="txt">(02) 5550 0148</div>
      </div>
      <div class="row" style="top:210px">
        <svg width="48" height="48" viewBox="0 0 48 48" fill="none" stroke="var(--orange)" stroke-width="3"><rect x="6" y="10" width="36" height="32" rx="3"/><path d="M6 20 h36 M16 5 v10 M32 5 v10"/><path d="M24 26 v6 h5"/></svg>
        <div class="txt">Monday to Friday 9am to 5pm</div>
      </div>
      <div class="map" role="img" aria-label="Circular street map marking the Harbour Point clinic"></div>
    </div>

    <div class="clinic">
      <div class="row" style="top:30px">
        <svg width="48" height="56" viewBox="0 0 48 56" fill="none" stroke="var(--orange)" stroke-width="3"><path d="M24 52 C10 34 8 28 8 20 a16 16 0 0 1 32 0 c0 8 -2 14 -16 32z"/><circle cx="24" cy="20" r="6"/><path d="M6 52 h36"/></svg>
        <div class="txt"><h3>ELM CROSSING</h3>Shop 4, 62 Linden Road<br>Elm Crossing</div>
      </div>
      <div class="row" style="top:130px">
        <svg width="48" height="48" viewBox="0 0 48 48" fill="none" stroke="var(--orange)" stroke-width="3" stroke-linejoin="round"><path d="M10 6 l8 0 l4 10 l-6 4 a26 26 0 0 0 12 12 l4 -6 l10 4 v8 a4 4 0 0 1 -4 4 C20 42 6 28 6 10 a4 4 0 0 1 4 -4z"/></svg>
        <div class="txt">(02) 5550 0263</div>
      </div>
      <div class="row" style="top:210px">
        <svg width="48" height="48" viewBox="0 0 48 48" fill="none" stroke="var(--orange)" stroke-width="3"><rect x="6" y="10" width="36" height="32" rx="3"/><path d="M6 20 h36 M16 5 v10 M32 5 v10"/><path d="M24 26 v6 h5"/></svg>
        <div class="txt">Monday to Friday 9am to 5pm</div>
      </div>
      <div class="map" role="img" aria-label="Circular street map marking the Elm Crossing clinic"></div>
    </div>
  </div>
</section>

<footer class="footer">
  <div class="wrap">
    <div class="quick">
      <h4>Quick Links</h4>
      <ul>
        <li>About Us</li>
        <li>Our Hearing</li>
        <li>Hearing Aids</li>
        <li>Resources</li>
        <li>Services Information</li>
      </ul>
    </div>
    <div class="contact-form">
      <h4>Contact Us</h4>
      <form>
        <div class="field">Name</div>
        <div class="field">Email</div>
        <div class="field">Subject</div>
        <div class="field msg">Message</div>
        <div class="btn">Send</div>
      </form>
    </div>
    <div class="social">
      <h4>Social Media</h4>
      <div class="icons"><span></span><span></span><span></span></div>
    </div>
  </div>
</footer>
<div class="legal">© Pelmora Hearing 2018</div>

</body>
</html>
```